A Real Estate Company Needs a Business Card Design

We need a business card design for a new company based in Boston MA called "Brackenfield Real Estate LLC" we are a small company but we like a big corporate look, a simple, sleek, modern and progressive look. we would like the option of having a design that could include the real estate agents personal photo and also a design if the realtor decides not to have a photo. we do not have LOGO at this moment, please use any property look pic corporate with word" Brackenfield Real Estate LLC" please see attached file as an example.
Industry/Entity Type
Business

```html
<!DOCTYPE html>
<html lang="en">
<head>
<meta charset="utf-8">
<title>Brackenfield Real Estate LLC – Business Cards</title>
<link href="https://fonts.googleapis.com/css2?family=Arimo:wght@400;700&display=swap" rel="stylesheet">
<style>
  :root {
    --stage: #3a2f3f;
    --card: #ffffff;
    --brand-blue: #1656b8;
    --band-dark: #0d2a78;
    --band-light: #1d5fb8;
    --accent-red: #e0202a;
    --frame-lime: #d8e05a;
    --photo-tone: #8f8a86;
    --ink: #1b1b1b;
    --on-band: #ffffff;
  }
  * { box-sizing: border-box; margin: 0; padding: 0; }
  html, body { width: 1200px; height: 800px; overflow: hidden; }
  body {
    background: var(--stage);
    font-family: "Arimo", Arial, sans-serif;
    display: flex;
    align-items: center;
    justify-content: center;
    gap: 60px;
  }
  .card {
    position: relative;
    width: 500px;
    height: 286px;
    background: var(--card);
    overflow: hidden;
    box-shadow: 0 12px 30px rgba(0,0,0,.35);
  }
  .brand {
    display: flex;
    align-items: center;
    gap: 12px;
    color: var(--brand-blue);
    font-weight: 700;
  }
  .brand-mark {
    width: 30px;
    height: 30px;
    background: var(--accent-red);
    flex: none;
  }
  .brand-name { line-height: 1.05; text-transform: uppercase; }
  .brand-name span { display: block; }

  /* back card */
  .card-back {
    display: flex;
    flex-direction: column;
    align-items: center;
    justify-content: center;
    gap: 22px;
  }
  .card-back .brand-name { font-size: 30px; letter-spacing: 1px; }
  .card-back .brand-name span + span { font-size: 18px; letter-spacing: 2px; }
  .website { font-size: 14px; color: var(--ink); }

  /* front card */
  .card-front { border-top: 6px solid var(--frame-lime); }
  .photo {
    position: absolute;
    left: 26px;
    top: 16px;
    width: 108px;
    height: 96px;
    border: 4px solid var(--frame-lime);
    background: linear-gradient(160deg, #a8a29c, var(--photo-tone));
  }
  .card-front .brand {
    position: absolute;
    right: 22px;
    top: 34px;
  }
  .card-front .brand-name { font-size: 26px; letter-spacing: 1px; }
  .card-front .brand-name span + span { font-size: 16px; letter-spacing: 1.5px; }
  .contact-band {
    position: absolute;
    left: 0; right: 0; bottom: 0;
    height: 150px;
    border-top: 4px solid var(--accent-red);
    background: linear-gradient(110deg, var(--band-dark), var(--band-light));
    color: var(--on-band);
  }
  .contact-band::before {
    content: "";
    position: absolute;
    left: 0; right: 0; top: 0;
    height: 3px;
    background: var(--card);
  }
  .agent { position: absolute; left: 26px; top: 24px; }
  .agent-name { font-size: 19px; }
  .agent-title { font-size: 12px; margin-top: 4px; }
  .divider { position: absolute; left: 236px; top: 30px; }
  .contact-list {
    position: absolute;
    left: 262px;
    top: 40px;
    list-style: none;
    font-size: 12.5px;
    line-height: 1.55;
  }
</style>
</head>
<body>
  <section class="card card-back">
    <div class="brand">
      <div class="brand-mark"></div>
      <div class="brand-name"><span>Brackenfield</span><span>Real Estate LLC</span></div>
    </div>
    <p class="website">www.brackenfieldre.com</p>
  </section>

  <section class="card card-front">
    <div class="photo" role="img" aria-label="Agent portrait photo"></div>
    <div class="brand">
      <div class="brand-mark"></div>
      <div class="brand-name"><span>Brackenfield</span><span>Real Estate LLC</span></div>
    </div>
    <div class="contact-band">
      <div class="agent">
        <p class="agent-name">Your name here</p>
        <p class="agent-title">Title here</p>
      </div>
      <svg class="divider" width="4" height="90" viewBox="0 0 4 90" aria-hidden="true">
        <line x1="2" y1="0" x2="2" y2="90" stroke="rgba(255,255,255,.55)" stroke-width="1"/>
      </svg>
      <ul class="contact-list">
        <li>Address line 1, address line 2</li>
        <li>Phone : 06172409318</li>
        <li>Fax : 06172409327</li>
        <li>Email : agent@brackenfieldre.com</li>
      </ul>
    </div>
  </section>
</body>
</html>
```